Redbrook Disposal ~ A+ Division of Ironclad

Energetic ,different ,exotic ,modern,
never before done, next level buisness card for a trash dumpster company
is for a trash removal construction company ...please have your wildest ideas i dont want a boring basic buisness card i want people to say wow !! And be able to mention you and who designed my card ...i know you take pride in your work i do to ....3 years ago quietfern from pixel harbor made a logo for me and i still love it .....use his colors and the word ironclad DO NOT USE ROOFING AND REMODELING use Redbrook Disposal ....look at his Logo i Like the [I] LOGO and word Ironclad ....you surprise me and we will do alot more projects with you and or pixel harbor ....thank you for your hard work and your time i do appreciate all of you and admire your skills designing .....i really do appreciate all of you thank you -dale
Ps Lets make these biz cards special different from many ,unique

Target Market(s)

Construction .....dumpsters trash Trash removal

Industry/Entity Type

Construction

Contact Information for Business Card

Black gold white maybe more colors

Requirements
Must have
• Ironclad ~Redbrook Disposal division Serving Atlanta and surrounding areas'Chief executive Dale Kimber cell 404 555 0172 Office 404 888 8888Follow us on fb ,instagram .. email Redbrookdisposal.example Hablamos espaƱol
Nice to have
• Black gold white colors like my logo i updated and you can add more if you want ....its a construction / trucking company dumpster Trash company we recycle also
Should not have
• When you look at my logo (Must not have roofing and remodeling )

```html
<!DOCTYPE html>
<html lang="en">
<head>
<meta charset="utf-8">
<title>Ironclad – Redbrook Disposal Division business card</title>
<link rel="stylesheet" href="https://fonts.googleapis.com/css2?family=Roboto+Condensed:wght@400;700&family=Roboto:wght@400;500&display=swap">
<style>
  :root {
    --ink: #1f1d1e;
    --paper: #f7f7f7;
    --gold: #e2ac1c;
    --gold-deep: #d9a51f;
    --gold-bright: #ffdc00;
    --white: #ffffff;
    --backdrop: #ece9e4;
  }
  * { margin: 0; padding: 0; box-sizing: border-box; }
  html, body { width: 1200px; height: 960px; overflow: hidden; }
  body {
    position: relative;
    background: var(--backdrop);
    font-family: "Roboto", Arial, sans-serif;
  }
  .card {
    position: absolute;
    width: 600px;
    height: 343px;
    overflow: hidden;
    box-shadow: 0 3px 8px rgba(0,0,0,.25);
  }
  .card-front { left: 302px; top: 129px; background: var(--paper); }
  .card-back {
    left: 299px; top: 488px; height: 342px;
    background: linear-gradient(180deg, var(--gold-deep) 0%, var(--gold-bright) 50%, var(--gold-deep) 100%);
  }
  .front-wave { position: absolute; inset: 0; }

  .brand { position: absolute; display: flex; align-items: center; }
  .brand-square { flex: none; }
  .brand-text { display: flex; flex-direction: column; }
  .brand-name {
    font-family: "Roboto Condensed", "Arial Narrow", sans-serif;
    font-weight: 700;
    line-height: 1;
    letter-spacing: 1px;
  }
  .brand-division {
    font-family: "Roboto Condensed", "Arial Narrow", sans-serif;
    font-weight: 700;
    letter-spacing: 2.4px;
    line-height: 1;
  }

  .card-front .brand { left: 100px; top: 43px; }
  .card-front .brand-square { width: 83px; height: 83px; background: var(--gold); margin-right: 13px; }
  .card-front .brand-name { font-size: 48px; color: var(--ink); }
  .card-front .brand-division { font-size: 13.5px; color: var(--gold); margin-top: 4px; }

  .holder {
    position: absolute; right: 338px; top: 216px;
    text-align: right; color: var(--white);
  }
  .holder-name {
    font-family: "Roboto Condensed", "Arial Narrow", sans-serif;
    font-size: 21px; color: var(--gold); line-height: 24px;
  }
  .holder-title {
    font-family: "Roboto Condensed", "Arial Narrow", sans-serif;
    font-size: 16px; line-height: 22px; letter-spacing: .3px;
  }
  .holder-address { font-size: 14px; line-height: 19px; }
  .divider {
    position: absolute; left: 280px; top: 218px;
    width: 1px; height: 78px; background: #5a5859;
  }
  .contacts {
    position: absolute; left: 300px; top: 220px;
    list-style: none; color: var(--white); font-size: 14px;
  }
  .contacts li { display: flex; align-items: center; height: 19.3px; }
  .contacts svg { width: 12px; height: 12px; margin-right: 8px; fill: var(--gold); }

  .card-back .brand { left: 121px; top: 125px; }
  .card-back .brand-square { width: 74px; height: 74px; background: var(--white); margin-right: 11px; }
  .card-back .brand-name { font-size: 43px; color: var(--white); }
  .card-back .brand-division { font-size: 12.5px; color: var(--white); margin-top: 3px; }

  .social {
    position: absolute; left: 238px; top: 277px;
    display: flex; gap: 3.5px; list-style: none;
  }
  .social li { width: 22px; height: 22px; border-radius: 50%; background: var(--white); }
</style>
</head>
<body>

<section class="card card-front" aria-label="Business card front">
  <svg class="front-wave" viewBox="0 0 600 343" preserveAspectRatio="none" aria-hidden="true">
    <path d="M0,116 C18,165 60,186 150,181 C260,173 380,141 480,151 C560,159 588,196 600,226 L600,343 L0,343 Z" fill="var(--ink)"/>
    <path d="M88,182 C200,176 330,140 450,143 C540,146 585,180 599,218 C580,188 540,160 470,156 C370,150 260,178 160,184 C130,186 105,185 88,182 Z" fill="var(--gold)"/>
  </svg>

  <div class="brand">
    <div class="brand-square"></div>
    <div class="brand-text">
      <span class="brand-name">IRONCLAD</span>
      <span class="brand-division">REDBROOK DISPOSAL DIVISION</span>
    </div>
  </div>

  <div class="holder">
    <p class="holder-name">DALE KIMBER</p>
    <p class="holder-title">CHIEF EXECUTIVE</p>
    <p class="holder-address">7421 Willowmere Lane</p>
    <p class="holder-address">Fairbanks, Alaska 34812</p>
  </div>

  <div class="divider"></div>

  <ul class="contacts">
    <li><svg viewBox="0 0 24 24"><path d="M6.6 10.8a15 15 0 0 0 6.6 6.6l2.2-2.2c.3-.3.7-.4 1-.2 1.1.4 2.3.6 3.6.6.6 0 1 .4 1 1V20c0 .6-.4 1-1 1A17 17 0 0 1 3 4c0-.6.4-1 1-1h3.5c.6 0 1 .4 1 1 0 1.3.2 2.5.6 3.6.1.3 0 .7-.2 1z"/></svg>404 555 0139</li>
    <li><svg viewBox="0 0 24 24"><path d="M7 1h10a2 2 0 0 1 2 2v18a2 2 0 0 1-2 2H7a2 2 0 0 1-2-2V3a2 2 0 0 1 2-2zm0 3v14h10V4zm5 15.5a1.2 1.2 0 1 0 0 2.4 1.2 1.2 0 0 0 0-2.4z"/></svg>404 555 0172</li>
    <li><svg viewBox="0 0 24 24"><path d="M2 5h20v14H2zm2 2v.5l8 5 8-5V7zm0 2.8V17h16V9.8l-8 5z"/></svg>dale@Redbrookdisposal.example</li>
    <li><svg viewBox="0 0 24 24"><circle cx="12" cy="12" r="10"/></svg>www.Redbrookdisposal.example</li>
  </ul>
</section>

<section class="card card-back" aria-label="Business card back">
  <div class="brand">
    <div class="brand-square"></div>
    <div class="brand-text">
      <span class="brand-name">IRONCLAD</span>
      <span class="brand-division">REDBROOK DISPOSAL DIVISION</span>
    </div>
  </div>

  <ul class="social" aria-label="Social media">
    <li></li><li></li><li></li><li></li><li></li>
  </ul>
</section>

</body>
</html>
```